Tempest Sealer - Postcard

tempestsealer.com

Tel ‪(941) 508-3174‬

Daniel Prewitt
daniel@tempestsealer.com

Design a postcard for a marketing campaign.

The problem is that all roofing vents leak. We have a product that goes into the vent that stops the roof from leaking.

In the last hurricane here in Florida, many houses were damaged because of water coming into the attic from the vents. The tempest sealer is a device that stops water from coming into the vents. This prevents water damage in the house. This stops mold from forming in the attic.

The tempest sealer offers this solution. It stops the rainwater from entering the roof through the roof vents. It stops water damages from occurring in the house which can cost 10s of thousands of dollars.

The target customer is a affluent, older couple 50-60 years old.

Target Market(s)

middle class to upper class adults / ages 50-60 years old (older but not VERY old)

Industry/Entity Type

roofing and construction

Font styles to use
Sans Serif

Colors
0054AA
0677BA
7BADD7
CADEEF
E8F1F8
0094D4
00A9DD
6FCCEA
C7EBF8
E9F6FB
FFF300
FFF600
FEFA6F
FFFEC7
FFFEE8
F0912C
F2A743
F7CA91
FBE8D2
FDF5EE

Requirements
Must have
• images of rain, wind, storm roofing, leaks, wet house, rain through interior ceilings, anxiety, storm damage
Nice to have
• feelings: professional / strong / reliable / safety / shelter / security / future stability

```html
<!DOCTYPE html>
<html lang="en">
<head>
<meta charset="utf-8">
<title>Tempest Sealer – Postcard</title>
<link rel="stylesheet" href="https://fonts.googleapis.com/css2?family=Montserrat:wght@400;500;600;700;800;900&family=Oswald:wght@600;700&display=swap">
<style>
  :root{
    --blue:#0054AA;
    --blue-deep:#0A4FB0;
    --yellow:#FFF300;
    --yellow-soft:#FEFA6F;
    --charcoal:#3A3F44;
    --ink:#1B1B1B;
    --panel:#E3E7EB;
    --stage:#B8B8B8;
    --white:#FFFFFF;
    --red:#E0262B;
  }
  *{margin:0;padding:0;box-sizing:border-box}
  html,body{width:1200px;height:2560px;overflow:hidden;background:var(--stage)}
  body{position:relative;font-family:"Montserrat",sans-serif;color:var(--ink)}
  .card{position:absolute;left:103px;width:1001px;height:668px;background:var(--white);overflow:hidden}
  .card--front{top:909px}
  .card--back{top:1640px}
  .abs{position:absolute}
  svg.abs{display:block}

  /* front */
  .brand{left:52px;top:50px;display:flex;align-items:center;gap:16px}
  .brand__dot{width:80px;height:80px;border-radius:50%;background:var(--ink)}
  .brand__name{font-weight:600;font-size:34px;line-height:1.05;color:var(--ink);letter-spacing:.5px}
  .hero-band{left:0;top:170px;width:520px;height:198px;background:var(--blue-deep)}
  .headline{left:54px;top:192px;color:var(--yellow);font-weight:900;text-transform:uppercase;line-height:1}
  .headline__a{font-size:56px;letter-spacing:1px}
  .headline__b{font-size:46px;letter-spacing:1px;margin-top:2px}
  .headline__c{color:var(--white);font-size:28px;font-weight:600;margin-top:8px;line-height:1.02}
  .intro{left:56px;top:383px;width:395px;font-size:14.2px;line-height:1.17;font-weight:500}
  .feature{left:60px;top:498px;display:flex;align-items:center;gap:18px}
  .icon-badge{width:68px;height:68px;border-radius:50%;background:var(--blue);display:flex;align-items:center;justify-content:center}
  .feature__text{font-size:30px;font-weight:500;line-height:1.02;color:var(--ink)}
  .feature__text b{color:var(--blue);font-weight:800}
  .cta-front{left:40px;top:610px;color:var(--white);display:flex;align-items:center;gap:12px}
  .cta__label{font-weight:900;font-size:26px;line-height:.95}
  .cta__label small{display:block;font-size:13.5px;font-weight:500;letter-spacing:.3px;margin-top:3px}
  .phone{font-family:"Oswald",sans-serif;font-weight:700;font-size:40px;letter-spacing:.5px}
  .web-front{left:580px;top:630px;font-size:23px;color:var(--ink)}
  .web-front b,.web-back b{font-weight:700}

  /* back */
  .back-panel{left:0;top:0;width:617px;height:668px;background:var(--panel)}
  .alert{left:42px;top:48px;width:445px;color:var(--white)}
  .alert__title{font-weight:900;font-size:21px;letter-spacing:.3px}
  .alert__body{font-size:15.2px;line-height:1.2;margin-top:3px;font-weight:500}
  .pitch{left:365px;top:220px;color:var(--blue)}
  .pitch__a{font-weight:900;font-size:43px;line-height:1}
  .pitch__b{font-weight:900;font-size:27px;line-height:1;margin-top:2px}
  .pitch__c{font-size:11px;color:#555;margin-top:4px;letter-spacing:.2px}
  .point{left:366px;display:flex;gap:10px;align-items:flex-start;font-size:13.6px;line-height:1.25;color:var(--ink)}
  .point .icon-badge{width:54px;height:54px;flex:none}
  .point--one{top:320px}
  .point--two{top:394px}
  .cta-back{left:326px;top:543px}
  .cta-back .cta__label{color:var(--ink);font-size:26px}
  .cta-back .cta__label small{font-size:13.5px}
  .cta-back__phone{display:flex;align-items:center;gap:8px;margin-top:2px;color:var(--blue)}
  .web-back{display:flex;align-items:center;gap:14px;font-size:16px;margin-top:2px;padding-left:4px}
</style>
</head>
<body>

<section class="card card--front">
  <svg class="abs" style="left:0;top:0" width="1001" height="668" viewBox="0 0 1001 668">
    <defs>
      <linearGradient id="room" x1="0" y1="0" x2="0" y2="1">
        <stop offset="0" stop-color="#DCD8D0"/><stop offset=".55" stop-color="#8E8B88"/><stop offset="1" stop-color="#6B6B70"/>
      </linearGradient>
      <linearGradient id="ceiling" x1="0" y1="0" x2="1" y2="1">
        <stop offset="0" stop-color="#D9CBB0"/><stop offset="1" stop-color="#F2F0EC"/>
      </linearGradient>
    </defs>
    <path d="M650 0 L1001 0 L1001 455 C950 560 860 610 760 610 C650 610 560 560 500 470 C470 420 455 350 462 290 C470 180 540 80 650 0 Z" fill="var(--charcoal)"/>
    <circle cx="830" cy="250" r="288" fill="var(--white)"/>
    <circle cx="830" cy="250" r="280" fill="url(#room)" role="img" aria-label="Photo: worried homeowner on a sofa, on the phone, catching a roof leak in a blue basin"/>
    <circle cx="570" cy="415" r="104" fill="var(--charcoal)"/>
    <circle cx="570" cy="415" r="95" fill="url(#ceiling)" role="img" aria-label="Photo: man holding a bucket under a water-damaged ceiling"/>
    <path d="M0 592 L470 592 C495 592 505 605 512 668 L0 668 Z" fill="var(--blue-deep)"/>
    <path d="M505 617 L1001 617 L1001 668 L518 668 C514 640 510 625 505 617 Z" fill="var(--yellow)"/>
  </svg>

  <div class="abs hero-band"></div>
  <div class="abs brand"><span class="brand__dot"></span><span class="brand__name">TEMPEST<br>SEALER</span></div>
  <div class="abs headline">
    <div class="headline__a">Protect</div>
    <div class="headline__b">Your Home</div>
    <div class="headline__c">With the Tempest<br>Sealer!</div>
  </div>
  <p class="abs intro">The TEMPEST SEALER is a proprietary system, engineered to block Wind Driven Rains from entering your Attic through the Rooftop Vents. The Tempest Sealer is made to withstand extreme conditions. Featuring StormWeave screening (an HVHZ approved material) and rigid steel construction.</p>
  <div class="abs feature">
    <span class="icon-badge">
      <svg width="40" height="40" viewBox="0 0 40 40" fill="none" stroke="var(--yellow)" stroke-width="2.4"><circle cx="20" cy="20" r="12"/><path d="M14 20l4 4 8-8"/></svg>
    </span>
    <p class="feature__text">CAN BE <b>INSTALLED</b><br>IN <b>ONE DAY!</b></p>
  </div>
  <div class="abs cta-front">
    <p class="cta__label">CALL TODAY<small>FOR SIMPLE PRICING!</small></p>
    <svg width="24" height="30" viewBox="0 0 24 30" fill="var(--yellow)"><path d="M6 4c2 0 3 5 2 7l-2 1c1 3 2 5 4 7l2-1c2 0 5 3 4 5l-2 3c-6 0-13-10-12-20z"/></svg>
    <span class="phone">941 508-3174</span>
  </div>
  <p class="abs web-front">www.<b>tempestsealer</b>.com</p>
</section>

<section class="card card--back">
  <div class="abs back-panel"></div>
  <svg class="abs" style="left:0;top:0" width="1001" height="668" viewBox="0 0 1001 668">
    <defs>
      <linearGradient id="couple" x1="0" y1="0" x2="1" y2="0">
        <stop offset="0" stop-color="#7F93A2"/><stop offset=".55" stop-color="#D8CFC4"/><stop offset="1" stop-color="#E6E8EA"/>
      </linearGradient>
      <linearGradient id="vent" x1="0" y1="0" x2="1" y2="1">
        <stop offset="0" stop-color="#8E9196"/><stop offset="1" stop-color="#C9CACC"/>
      </linearGradient>
    </defs>
    <rect x="617" y="0" width="384" height="668" fill="var(--white)"/>
    <rect x="0" y="205" width="360" height="330" fill="url(#couple)" role="img" aria-label="Photo: smiling older couple holding a small model house"/>
    <path d="M0 0 L692 0 C600 60 520 150 380 190 C250 220 100 205 0 185 Z" fill="var(--blue-deep)"/>
    <path d="M0 178 C100 200 220 205 320 200 C220 212 100 215 0 205 Z" fill="var(--red)"/>
    <path d="M0 535 L617 535 L617 668 L0 668 Z" fill="var(--yellow)"/>
    <path d="M0 540 L225 540 L305 668 L0 668 Z" fill="url(#vent)" role="img" aria-label="Photo: perforated steel roof vent insert"/>
  </svg>

  <div class="abs alert">
    <p class="alert__title">ALL ROOF VENTS LEAK!</p>
    <p class="alert__body">Any Winds over 30 MPH can push Wind &amp; Rain into your Attic through the Roof Vents! The result is Water Damage that can cost Thousands of Dollars in Remediation and Repairs.</p>
  </div>
  <div class="abs pitch">
    <p class="pitch__a">PROTECT</p>
    <p class="pitch__b">YOUR HOME!</p>
    <p class="pitch__c">CALL TODAY FOR SIMPLE PRICING!</p>
  </div>
  <div class="abs point point--one">
    <span class="icon-badge"><svg width="32" height="32" viewBox="0 0 32 32" fill="none" stroke="var(--yellow)" stroke-width="2.2"><circle cx="16" cy="16" r="10"/><circle cx="16" cy="16" r="4"/></svg></span>
    <p>All Roof Vents Leak!<br>Get The Tempest<br>Sealer!</p>
  </div>
  <div class="abs point point--two">
    <span class="icon-badge"><svg width="32" height="32" viewBox="0 0 32 32" fill="none" stroke="var(--yellow)" stroke-width="2.2"><circle cx="16" cy="16" r="10"/><path d="M11 16l4 4 6-7"/></svg></span>
    <p>Can be installed in<br>ONE DAY!<br><span style="display:block;margin-top:8px">CALL NOW for<br>Scheduling!</span></p>
  </div>
  <div class="abs cta-back">
    <p class="cta__label">CALL TODAY<small>FOR SCHEDULING!</small></p>
    <div class="cta-back__phone">
      <svg width="24" height="30" viewBox="0 0 24 30" fill="var(--ink)"><path d="M6 4c2 0 3 5 2 7l-2 1c1 3 2 5 4 7l2-1c2 0 5 3 4 5l-2 3c-6 0-13-10-12-20z"/></svg>
      <span class="phone">941 508-3174</span>
    </div>
    <p class="web-back">
      <svg width="14" height="14" viewBox="0 0 14 14" fill="none" stroke="var(--ink)" stroke-width="1.2"><circle cx="7" cy="7" r="6"/><path d="M1 7h12M7 1c3 3 3 9 0 12M7 1c-3 3-3 9 0 12"/></svg>
      <span>www.<b>tempestsealer</b>.com</span>
    </p>
  </div>
</section>

</body>
</html>
```